Yard Sign Design Needed

Yard sign needed for mowing & landscaping company. Would like to use the top logo with black background which is attached. Would like MOWING to be in large standout letters. The word "landscaping" can be smaller and more artistic or omitted. Will need room for phone number once design is approved. The phone number will need to stand out and look identical/similar to the word 'MOWING"

```html
<!DOCTYPE html>
<html lang="en">
<head>
<meta charset="utf-8">
<title>Braven Contractors – Mowing Yard Sign</title>
<link rel="stylesheet" href="https://fonts.googleapis.com/css2?family=Michroma&display=swap">
<style>
  :root {
    --ink: #060606;
    --lime: #a2c93a;
    --paper: #ffffff;
    --backdrop: #e8e8e6;
  }
  * { margin: 0; padding: 0; box-sizing: border-box; }
  html, body {
    width: 1200px;
    height: 2590px;
    overflow: hidden;
    background: var(--backdrop);
  }
  .canvas {
    position: relative;
    width: 1200px;
    height: 2590px;
  }
  .yard-sign {
    position: absolute;
    left: 30px;
    top: 532px;
    width: 1140px;
    height: 1526px;
    box-shadow: 0 20px 40px rgba(0,0,0,0.25);
  }
  .yard-sign svg { display: block; width: 100%; height: 100%; }
  .sign-text { font-family: "Michroma", sans-serif; }
  .brand-mark { fill: var(--lime); }
  .brand-name { fill: var(--lime); }
  .headline { fill: var(--ink); stroke: var(--ink); stroke-width: 2.5; }
  .subhead { fill: var(--lime); }
  .phone-pill { fill: var(--lime); stroke: var(--ink); stroke-width: 3; }
  .phone-badge { fill: var(--ink); stroke: var(--paper); stroke-width: 3; }
  .phone-icon { fill: var(--paper); }
  .phone-number { fill: var(--ink); stroke: var(--ink); stroke-width: 1.5; }
</style>
</head>
<body>
<main class="canvas">
  <section class="yard-sign" aria-label="Mowing and landscaping yard sign">
    <svg viewBox="0 0 814 1090" xmlns="http://www.w3.org/2000/svg">
      <!-- panels -->
      <rect class="top-panel" x="0" y="0" width="814" height="700" fill="var(--ink)"/>
      <path class="swoosh" d="M0,545 C200,440 560,420 814,660 L814,672 C560,500 230,520 0,672 Z" fill="var(--lime)"/>
      <path class="lower-panel" d="M0,680 C230,528 560,508 814,680 L814,1090 L0,1090 Z" fill="var(--paper)"/>

      <!-- brand -->
      <rect class="brand-mark" x="352" y="95" width="110" height="110"/>
      <text class="sign-text brand-name" x="407" y="365" text-anchor="middle" font-size="72"
            textLength="380" lengthAdjust="spacingAndGlyphs">BRAVEN</text>
      <text class="sign-text brand-name" x="407" y="418" text-anchor="middle" font-size="30"
            textLength="390" lengthAdjust="spacingAndGlyphs">CONTRACTORS LLC</text>

      <!-- headline -->
      <text class="sign-text headline" x="73" y="787" font-size="100"
            textLength="667" lengthAdjust="spacingAndGlyphs">MOWING</text>
      <text class="sign-text subhead" x="73" y="845" font-size="36"
            textLength="667" lengthAdjust="spacing">LANDSCAPING</text>

      <!-- phone -->
      <rect class="phone-pill" x="70" y="932" width="675" height="98" rx="49"/>
      <circle class="phone-badge" cx="120" cy="981" r="31"/>
      <path class="phone-icon" d="M107,966 l7,-3 l6,10 l-5,4 c2,6 6,10 12,13 l4,-5 l10,6 l-3,7 c-16,2 -33,-16 -31,-32 z"/>
      <text class="sign-text phone-number" x="170" y="1004" font-size="56"
            textLength="525" lengthAdjust="spacingAndGlyphs">5550-123-987</text>
    </svg>
  </section>
</main>
</body>
</html>
```